Ridgeway Talent Associates Business Card Design

We need a business card design for our new company - Ridgeway Talent Associates. RWTA is a recruitment firm that focuses on recruiting engineers and geologist for mid-size oil and gas companies. We would like our logo on the business card, which is attached, and we would like the color scheme on business cards to coordinate with our logo.

Industry/Entity Type

Oil And Gas

Contact Information for Business Card

Dana Whitfield, Founder and Managing Partner, dlw@ridgewaytalenthub.org, 888.574.2093 (work), 8140619.4372 (cell), 814.752.6190 (fax), www.ridgewaytalenthub.org

```html
<!DOCTYPE html>
<html lang="en">
<head>
<meta charset="utf-8">
<title>Ridgeway Talent Associates – Business Cards</title>
<link rel="stylesheet" href="https://fonts.googleapis.com/css2?family=Cinzel:wght@400;600&family=Lato:wght@400;700&display=swap">
<style>
  :root {
    --stage: #2b2b2b;
    --navy: #1a2a7c;
    --navy-deep: #121d5e;
    --navy-ink: #1f3478;
    --paper: #ffffff;
    --paper-shade: #eef0f3;
    --ghost: #d9dde3;
    --icon-bg: #c9cfe6;
  }
  * { box-sizing: border-box; margin: 0; padding: 0; }
  html, body { width: 1200px; height: 997px; overflow: hidden; }
  body { background: var(--stage); position: relative; font-family: "Lato", sans-serif; }

  .card {
    position: absolute;
    width: 640px; height: 366px;
    border-radius: 22px;
    overflow: hidden;
    background: linear-gradient(180deg, var(--paper) 0%, var(--paper-shade) 100%);
    box-shadow: 0 18px 40px rgba(0,0,0,.55);
  }
  .card--front { left: 80px; top: 90px; }
  .card--back  { left: 480px; top: 530px; }

  .band { position: absolute; left: 0; right: 0; background: var(--navy); }
  .card--front .band--top    { top: 0; height: 42px; }
  .card--front .band--bottom { bottom: 0; height: 42px; }

  .ghost-mark {
    position: absolute; border-radius: 50%;
    background: var(--ghost); opacity: .55;
  }
  .card--front .ghost-mark { width: 230px; height: 230px; left: -40px; top: 90px; }
  .card--back .ghost-mark  { width: 210px; height: 210px; left: -30px; top: 20px; }

  .brand { position: absolute; display: flex; align-items: center; gap: 12px; }
  .brand__dot { width: 30px; height: 30px; border-radius: 50%; background: var(--navy-ink); flex: none; }
  .brand__name {
    font-family: "Cinzel", serif; font-weight: 600;
    font-size: 25px; color: var(--navy-ink); letter-spacing: .5px; white-space: nowrap;
  }
  .card--front .brand { left: 170px; top: 164px; }
  .card--back .brand  { left: 150px; top: 62px; }

  .holder { position: absolute; right: 40px; top: 122px; text-align: right; }
  .holder__name {
    font-family: "Cinzel", serif; font-weight: 400;
    font-size: 24px; color: var(--navy-ink); letter-spacing: 1px;
  }
  .holder__title {
    font-family: "Lato", sans-serif; font-weight: 700;
    font-size: 13px; color: #6b7490; text-transform: uppercase; letter-spacing: .5px; margin-top: 2px;
  }

  .card--back .panel {
    position: absolute; left: 0; right: 0; bottom: 0; height: 190px;
    background: linear-gradient(180deg, var(--navy) 0%, var(--navy-deep) 100%);
  }
  .contacts {
    position: absolute; left: 32px; right: 32px; top: 212px;
    display: grid; grid-template-columns: 1.05fr 1.3fr 1fr; row-gap: 26px; column-gap: 14px;
    list-style: none;
  }
  .contacts__item { display: flex; align-items: center; gap: 9px; color: #e4e8f4; font-size: 17px; font-weight: 700; white-space: nowrap; }
  .contacts__item--wide { grid-column: 1 / span 3; }
  .contacts__icon {
    width: 26px; height: 26px; border-radius: 50%; background: var(--icon-bg);
    display: flex; align-items: center; justify-content: center; flex: none;
  }
  .contacts__icon svg { width: 15px; height: 15px; fill: var(--navy-deep); }
</style>
</head>
<body>

  <section class="card card--front" aria-label="Card front">
    <div class="band band--top"></div>
    <div class="ghost-mark"></div>
    <div class="brand">
      <span class="brand__dot"></span>
      <span class="brand__name">Ridgeway Talent Associates</span>
    </div>
    <div class="band band--bottom"></div>
  </section>

  <section class="card card--back" aria-label="Card back">
    <div class="ghost-mark"></div>
    <div class="brand">
      <span class="brand__dot"></span>
      <span class="brand__name">Ridgeway Talent Associates</span>
    </div>
    <div class="holder">
      <p class="holder__name">DANA WHITFIELD</p>
      <p class="holder__title">Founder &amp; Managing Partner</p>
    </div>
    <div class="panel"></div>
    <ul class="contacts">
      <li class="contacts__item">
        <span class="contacts__icon"><svg viewBox="0 0 16 16"><path d="M2 5c0-2 2-3 6-3s6 1 6 3l-2 1-1-2H5L4 6 2 5zm2 2h8l1 6H3l1-6zm4 1.5a2 2 0 100 4 2 2 0 000-4z"/></svg></span>
        888.574.2093
      </li>
      <li class="contacts__item">
        <span class="contacts__icon"><svg viewBox="0 0 16 16"><path d="M5 1h6a1 1 0 011 1v12a1 1 0 01-1 1H5a1 1 0 01-1-1V2a1 1 0 011-1zm0 2v9h6V3H5zm3 10a.8.8 0 100 1.6.8.8 0 000-1.6z"/></svg></span>
        8140619.4372
      </li>
      <li class="contacts__item">
        <span class="contacts__icon"><svg viewBox="0 0 16 16"><path d="M4 1h6l2 2v3H4V1zm-2 6h12a1 1 0 011 1v5H1V8a1 1 0 011-1zm2 4v4h8v-4H4z"/></svg></span>
        814.752.6190
      </li>
      <li class="contacts__item contacts__item--wide">
        <span class="contacts__icon"><svg viewBox="0 0 16 16"><path d="M1 3h14v10H1V3zm1.5 1.2L8 8.6l5.5-4.4H2.5zM2 5.3V12h12V5.3L8 10 2 5.3z"/></svg></span>
        info@ridgewaytalenthub.org
      </li>
    </ul>
  </section>

</body>
</html>
```